TBNW site redesign

Please redesign a home page with content provided. PSD only - no coding
Can use any images from Vexelmarq.com

Please create a site design that more clearly illustrates the client's services and expertise. We are looking for a high-end design.

Any images used must be generic or of Dallas TX.

Fonts: Any
Colors: Match to logo
Look: Modern - Professional

Target Market(s)

medium-large business owners

Number of Pages Required

1 page

Font styles to use
Serif
Sans Serif

Requirements
Must have
• cohesive professional design
• high end look
• Match to logo

```html
<!DOCTYPE html>
<html lang="en">
<head>
<meta charset="utf-8">
<title>TBNW – Why Tenant Presentation</title>
<link href="https://fonts.googleapis.com/css2?family=Cinzel:wght@600;700&family=Arimo&display=swap" rel="stylesheet">
<style>
  :root {
    --page-bg: #f2f2f4;
    --red-dark: #cc1f27;
    --red-light: #d92e34;
    --white: #ffffff;
    --ink: #1a1a1a;
  }
  * { margin: 0; padding: 0; box-sizing: border-box; }
  html, body { width: 1200px; height: 1000px; overflow: hidden; background: var(--page-bg); }
  .site {
    position: absolute; left: 0; top: 125px;
    width: 1200px; height: 749px;
    background: var(--white); overflow: hidden;
    font-family: "Arimo", Arial, sans-serif; color: var(--ink);
  }
  .nav-band { position: absolute; left: 0; top: 0; width: 1200px; height: 192px; }
  .nav-band svg { position: absolute; left: 0; top: 0; }
  .nav-label {
    position: absolute; top: 66px; width: 230px; margin-left: -115px;
    text-align: center; color: var(--white);
    font-family: "Cinzel", Georgia, serif; font-weight: 700;
    font-size: 21px; line-height: 32px; letter-spacing: 1px;
  }
  .section-title {
    position: absolute; color: var(--red-dark);
    font-family: "Cinzel", Georgia, serif; font-weight: 700; letter-spacing: 0.5px;
  }
  .why-title { left: 44px; top: 250px; font-size: 28px; }
  .team-title { left: 54px; top: 662px; font-size: 34px; }
  .point { position: absolute; font-size: 21px; line-height: 27px; }
  .point h3 { font-weight: 400; font-size: 21px; margin-bottom: 22px; }
  .point p { margin: 0; }
  .relationships { left: 56px; top: 294px; width: 520px; }
  .access { left: 56px; top: 468px; width: 530px; }
  .access h3 { margin-bottom: 18px; }
  .access p { margin-left: -3px; }
  .free { left: 673px; top: 294px; width: 500px; }
  .free h3 { margin-bottom: 18px; }
  .custom { left: 671px; top: 433px; width: 500px; }
  .custom h3 { margin-bottom: 24px; }
</style>
</head>
<body>
<main class="site">
  <header class="nav-band">
    <svg width="1200" height="192" viewBox="0 0 1200 192" aria-hidden="true">
      <rect width="1200" height="192" fill="var(--red-dark)"/>
      <polygon points="513,0 1200,0 1200,192 657,192" fill="var(--red-light)"/>
      <circle cx="277" cy="-9" r="42" fill="#fff"/>
      <circle cx="277" cy="8" r="5" fill="var(--red-dark)"/>
      <circle cx="492" cy="-9" r="42" fill="#fff"/>
      <circle cx="492" cy="-9" r="31" fill="var(--red-dark)"/>
      <rect x="478" y="0" width="28" height="12" fill="#fff"/>
      <rect x="484" y="2" width="4" height="4" fill="var(--red-dark)"/>
      <rect x="490" y="2" width="4" height="4" fill="var(--red-dark)"/>
      <rect x="496" y="2" width="4" height="4" fill="var(--red-dark)"/>
      <circle cx="723" cy="-9" r="42" fill="#fff"/>
      <polygon points="712,6 734,6 748,16 698,16" fill="var(--red-light)"/>
      <circle cx="946" cy="-9" r="42" fill="#fff"/>
      <rect x="934" y="-2" width="24" height="12" rx="2" fill="var(--red-light)"/>
      <rect x="939" y="2" width="14" height="2" fill="#fff"/>
    </svg>
    <div class="nav-label" style="left:277px">Why Tenant<br>Presentation</div>
    <div class="nav-label" style="left:492px">Meet the<br>Team</div>
    <div class="nav-label" style="left:723px">Client<br>Testimonial</div>
    <div class="nav-label" style="left:946px">Recent<br>Articles</div>
  </header>

  <h2 class="section-title why-title">WHY TENANT PRESENTATION</h2>

  <section class="point relationships">
    <h3>Relationships:</h3>
    <p>Save time by trusting TBNW year after year to find the right location for you. Once we’ve worked together, we know what you need, and you can keep your budget details private.</p>
  </section>

  <section class="point access">
    <h3>Access to More:</h3>
    <p>We have no agreements or personal incentives for specific properties, so we can always show you the offices that are right for you.</p>
  </section>

  <section class="point free">
    <h3>Free To You:</h3>
    <p>You pay us nothing. We get our commission from the property being leased.</p>
  </section>

  <section class="point custom">
    <h3>Customized Service:</h3>
    <p>Aside from saving you the time of repeating what your needs are to each new location, we also provide a report of the places you’ve seen, so it’s easier to share and make a decision.</p>
  </section>

  <h2 class="section-title team-title">Meet the team</h2>
</main>
</body>
</html>
```